Satin Decor Paint Label

We will have three different sizes for this label but the dimensions for the medium size are 2" tall by 11.75'' wide. Please work off that.

Our colors are typically black and white but feel free to incorporate silver, gold, bronze or any combination. We would like to see multiple color variations of your designs.

General Info needed on label:
2736
Coatings
Interior Decor Paint
Furniture, Trim, Cabinets
Acrylic Waterborne Urethane
Satin Finish
16 FL. OZ. - 473 mL
````````````````````````````````````````````````````````````````````````````````````````````
Your design does not have to be the same as the one in the attached image.

You can put Satin Finish or Interior Decor Paint or something else going vertically up the side.

The label will be on a container like the the one in the attached image. Please have your design work on the same container.

```html
<!DOCTYPE html>
<html lang="en">
<head>
<meta charset="UTF-8">
<title>2736 Coatings – Satin Decor Paint Label</title>
<link href="https://fonts.googleapis.com/css2?family=Open+Sans:wght@400;700&display=swap" rel="stylesheet">
<style>
  :root {
    --backdrop: #e4e4e4;
    --label-black: #0c0c0c;
    --label-white: #f2f2f2;
    --rule-grey: #9a9a9a;
  }
  * { margin: 0; padding: 0; box-sizing: border-box; }
  html, body {
    width: 849px;
    height: 1200px;
    overflow: hidden;
    background: var(--backdrop);
    font-family: "Open Sans", Arial, sans-serif;
  }
  .canvas {
    position: relative;
    width: 849px;
    height: 1200px;
    display: flex;
    align-items: center;
    justify-content: center;
  }
  .label {
    position: relative;
    width: 640px;
    height: 460px;
    background: var(--label-black);
    color: var(--label-white);
  }
  .info-frame {
    position: absolute;
    left: 150px;
    top: 60px;
    width: 300px;
    height: 300px;
    border: 1.5px solid var(--label-white);
    display: flex;
    flex-direction: column;
    align-items: center;
    justify-content: center;
    text-align: center;
    padding-bottom: 10px;
  }
  .brand-name {
    font-size: 40px;
    font-weight: 400;
    line-height: 1.1;
    white-space: nowrap;
  }
  .brand-rule {
    width: 236px;
    height: 1px;
    background: var(--rule-grey);
    margin: 22px auto 18px;
  }
  .product-uses {
    font-size: 17px;
    font-weight: 400;
    line-height: 1.45;
    letter-spacing: 0.3px;
    white-space: nowrap;
  }
  .finish-tag {
    position: absolute;
    left: 50%;
    bottom: -14px;
    transform: translateX(-50%);
    background: var(--label-white);
    color: var(--label-black);
    font-weight: 700;
    font-size: 16px;
    letter-spacing: 0.5px;
    padding: 3px 26px;
    white-space: nowrap;
  }
  .volume {
    position: absolute;
    left: 150px;
    width: 300px;
    top: 382px;
    text-align: center;
    font-size: 17px;
    letter-spacing: 0.5px;
  }
  .side-title {
    position: absolute;
    left: 476px;
    top: 360px;
    transform-origin: left top;
    transform: rotate(-90deg);
    width: 300px;
    font-size: 23px;
    font-weight: 400;
    letter-spacing: 1px;
    white-space: nowrap;
  }
</style>
</head>
<body>
  <main class="canvas">
    <section class="label" aria-label="Satin decor paint label">
      <div class="info-frame">
        <h1 class="brand-name">2736 Coatings</h1>
        <div class="brand-rule"></div>
        <p class="product-uses">FURNITURE, TRIM, CABINETS<br>ACRYLIC WATERBORNE URETHANE</p>
        <p class="finish-tag">SATIN FINISH</p>
      </div>
      <p class="volume">16 FL. OZ. - 473 mL</p>
      <p class="side-title">INTERIOR DECOR PAINT</p>
    </section>
  </main>
</body>
</html>
```